Begegnungskonzert Kammerchor Lumivessa Berlin und Tonbrückener Kinderchor Peking
Zielgruppe
Es geht um ein Konzertplakat für den Kammerchor Lumivessa Berlin. www.lumivessa-chor.example
Wir haben ein Begegnungskonzert mit einem Chinesischen Kinderchor, der Berlin besucht.
Aufgabenstellung
Kammerchor Lumivessa Berlin, Leitung: Karsten Brodt
Tonbrückener Kinderchor Peking, Leitung: Prof. Zhou Wen
21.08.2017, 19:00 Uhr Quellkapelle Berlin Wilmersdorf, Falkenauer Str. 27, 14183 Berlin
Eintritt frei, Spenden erbeten
Werke von Albrechtsen, Caspo, Thornvik, Pemberley und vielen mehr...
Logos und Farben bitte von unserer Website übernehmen!

```html
<!DOCTYPE html>
<html lang="de">
<head>
<meta charset="utf-8">
<title>Begegnungskonzert Berlin // Peking</title>
<link href="https://fonts.googleapis.com/css2?family=Roboto:wght@300;400;500;700&display=swap" rel="stylesheet">
<style>
  :root {
    --ink: #1b1b1b;
    --paper: #ffffff;
    --backdrop: #e9e9e7;
    --stage-warm: #b98e5c;
    --stage-dark: #3a2a22;
    --wood-light: #f1d9bd;
    --veil: rgba(120,120,120,0.45);
  }
  html, body {
    margin: 0;
    width: 1200px;
    height: 928px;
    overflow: hidden;
    background: var(--backdrop);
    font-family: "Roboto", Arial, sans-serif;
  }
  .poster-stage {
    position: absolute;
    left: 294px;
    top: 24px;
    width: 574px;
    height: 826px;
    transform: scale(1.065);
    transform-origin: 0 0;
    background: var(--paper);
    overflow: hidden;
    box-shadow: 0 6px 18px rgba(0,0,0,0.18);
  }
  .poster-shapes { position: absolute; inset: 0; }
  .choir-block, .event-title, .event-meta, .repertoire, .brand-name {
    position: absolute;
    color: var(--ink);
    margin: 0;
  }
  .choir-block { right: 34px; text-align: right; }
  .choir-block--berlin { top: 37px; }
  .choir-block--peking { top: 100px; }
  .choir-name {
    font-weight: 500;
    font-size: 14px;
    line-height: 17px;
    text-transform: uppercase;
  }
  .choir-lead { font-weight: 300; font-size: 10.5px; line-height: 14px; }
  .brand-name {
    left: 34px;
    top: 86px;
    color: var(--paper);
    font-weight: 400;
    font-size: 15px;
    line-height: 16px;
  }
  .event-title {
    left: 35px;
    top: 398px;
    font-weight: 700;
    font-size: 42px;
    line-height: 44px;
    letter-spacing: 0.3px;
  }
  .event-meta { left: 35px; top: 746px; }
  .event-date { font-weight: 500; font-size: 14px; line-height: 17px; }
  .event-place { font-weight: 300; font-size: 10.5px; line-height: 15px; }
  .repertoire { right: 34px; top: 729px; text-align: right; }
  .repertoire-intro { font-weight: 300; font-size: 10.5px; line-height: 14px; }
  .repertoire-list { font-weight: 500; font-size: 14px; line-height: 16.5px; }
</style>
</head>
<body>
  <div class="poster-stage">
    <svg class="poster-shapes" width="574" height="826" viewBox="0 0 574 826">
      <defs>
        <linearGradient id="stageUpper" x1="0" y1="0" x2="1" y2="1">
          <stop offset="0" stop-color="#9c7a55"/>
          <stop offset="0.5" stop-color="#5a3c30"/>
          <stop offset="1" stop-color="#1e1e2c"/>
        </linearGradient>
        <linearGradient id="stageLower" x1="0" y1="0" x2="0" y2="1">
          <stop offset="0" stop-color="#6b4a35"/>
          <stop offset="0.35" stop-color="#d9b48c"/>
          <stop offset="0.75" stop-color="#ecd2b3"/>
          <stop offset="1" stop-color="#f6e7d6"/>
        </linearGradient>
      </defs>
      <polygon class="brand-wedge" points="0,22 244,95 0,165" fill="var(--ink)"/>
      <polygon class="photo-children-choir" role="img"
        aria-label="Foto: Dirigent vor dem Kinderchor in Uniform"
        points="0,165 244,95 574,195 574,465 0,345" fill="url(#stageUpper)"/>
      <polygon class="title-wedge" points="0,345 60,330 574,465 0,600" fill="var(--paper)"/>
      <polygon class="photo-chamber-choir" role="img"
        aria-label="Foto: Kammerchor mit Dirigent auf der Konzertbühne"
        points="0,625 574,450 574,826 0,826" fill="url(#stageLower)"/>
      <polygon class="veil-wedge" points="330,530 574,450 574,600" fill="var(--veil)"/>
      <polygon class="title-wedge-lower" points="0,600 360,527 0,625" fill="var(--paper)"/>
    </svg>

    <p class="brand-name">Lumivessa<br>Berlin</p>

    <div class="choir-block choir-block--berlin">
      <div class="choir-name">Kammerchor Lumivessa<br>Berlin</div>
      <div class="choir-lead">Leitung: Karsten Brodt</div>
    </div>
    <div class="choir-block choir-block--peking">
      <div class="choir-name">Tonbrückener Kinderchor<br>Peking</div>
      <div class="choir-lead">Leitung: Prof. Zhou Wen</div>
    </div>

    <h1 class="event-title">BEGEGNUNGS-<br>KONZERT<br>BERLIN//PEKING</h1>

    <div class="event-meta">
      <div class="event-date">21. AUGUST 2017 // 19 UHR</div>
      <div class="event-place">Quellkapelle Berlin-Wilmersdorf<br>Falkenauer Str. 27 // 14183 Berlin</div>
    </div>

    <div class="repertoire">
      <div class="repertoire-intro">Werke von</div>
      <div class="repertoire-list">ALBRECHTSEN, CASPO,<br>THORNVIK, PEMBERLEY<br>UND VIELEN MEHR</div>
    </div>
  </div>
</body>
</html>
```